Building and Facilities Management brochure

Please refer to attached PDF, page by page with information about the brief.
SOPHISTICATED, BOLD, PROFESSIONAL BROCHURE to market our company in business meetings to Builders, Owners of buildings, Strata Committees etc.

The final design should portray quality, service, integrity,
Clear Communication

Attached is:
- pdf with details of basic layout options and wording and most of the information about the brief.
- Logo options to use
- Business card designs to understand what design we have previously had.
- Word document of the pdf if that helps to copy the information.

Target Market(s)

Professionals. Builders/developer, Strata Owners, and Building owners who want a high level of service and management of their building

Industry/Entity Type

It Company

Requirements
Must have
• - Logo
• - Contact details
• - Use of the colour in the design which has been specified.
• - Images/s of building/s
• - Use the phrase "Quality Service with Integrity"
Nice to have
• - as much of the wording as possible from the document which was uploaded, that will fit and work with the design
Should not have
• Excessive colour or variances as it needs to stay clear, bold and sophisticated.
• Too much on the page, clarity is key for clear communication without trying to clutter too much on the page.

```html
<!DOCTYPE html>
<html lang="en">
<head>
<meta charset="utf-8">
<title>Harlow Property Solutions – Brochure</title>
<link href="https://fonts.googleapis.com/css2?family=Montserrat:wght@300;400;600;700&display=swap" rel="stylesheet">
<style>
  :root{
    --brand:#2a9fd8;
    --brand-deep:#1a7fc0;
    --night:#0f2a5c;
    --night-deep:#071634;
    --ink:#4a4f57;
    --muted:#8a9099;
    --paper:#ffffff;
    --stage:#dcdcdc;
  }
  *{box-sizing:border-box;margin:0;padding:0}
  html,body{width:960px;height:1200px;overflow:hidden}
  body{
    background:radial-gradient(ellipse at 50% 40%,#f2f2f2 0%,var(--stage) 100%);
    font-family:'Montserrat',sans-serif;color:var(--ink);position:relative;
  }
  .spread{position:absolute;left:100px;width:760px;height:500px;display:flex;box-shadow:0 18px 40px rgba(0,0,0,.22)}
  .spread--cover{top:50px}
  .spread--inside{top:630px}
  .page{position:relative;width:380px;height:500px;overflow:hidden;background:var(--paper)}

  /* back cover */
  .back{background:linear-gradient(135deg,#35aee3 0%,var(--brand) 55%,var(--brand-deep) 100%);color:#fff}
  .back__city{position:absolute;right:0;top:90px;width:170px;height:200px;
    background:linear-gradient(180deg,rgba(20,60,120,0) 0%,rgba(20,60,120,.35) 60%,rgba(42,159,216,0) 100%)}
  .back__motto{position:absolute;left:40px;top:60px;font-size:40px;font-weight:300;line-height:1.05;
    text-transform:uppercase;color:rgba(20,70,130,.14);letter-spacing:1px}
  .back__name{position:absolute;left:0;right:0;top:250px;text-align:center;font-size:15px;font-weight:400;
    letter-spacing:2px;text-transform:uppercase}
  .back__contact{position:absolute;left:40px;bottom:36px;font-size:8px;line-height:1.8}

  /* front cover */
  .front__name{position:absolute;left:0;right:0;top:48px;text-align:center;font-size:13px;font-weight:400;
    letter-spacing:2px;text-transform:uppercase;color:var(--brand)}
  .front__name::before{content:"";display:inline-block;width:8px;height:8px;background:var(--brand);margin-right:8px;vertical-align:1px}
  .front__photo{position:absolute;left:0;right:0;top:130px;bottom:0;
    background:linear-gradient(180deg,#fff 0%,#8ea6c9 18%,#3d5a91 45%,#1a3470 70%,var(--night) 100%)}
  .front__tagline{position:absolute;right:28px;top:330px;text-align:right;color:#fff;text-transform:uppercase;
    font-weight:400;font-size:22px;line-height:1.15;letter-spacing:1px}
  .front__tagline small{font-size:15px}
  .front__url{position:absolute;right:28px;bottom:28px;color:#fff;font-size:8px}

  /* inside */
  .band{position:absolute;left:0;right:0;top:0;height:110px;
    background:linear-gradient(180deg,#3a5f9a 0%,#1e3b72 55%,var(--night-deep) 100%)}
  .band__title{position:absolute;left:24px;bottom:10px;color:#fff;font-size:24px;font-weight:300}
  .copy{font-size:7px;line-height:1.5;color:var(--ink)}
  .vision{position:absolute;left:24px;right:24px;top:124px}
  .vision p+p{margin-top:7px}
  .h-section{position:absolute;left:24px;top:250px;font-size:22px;font-weight:300;color:var(--brand)}
  .aspects{position:absolute;top:295px;width:160px}
  .aspects--a{left:24px}
  .aspects--b{left:200px;top:260px}
  .aspect{margin-bottom:10px}
  .aspect b{font-weight:700;text-transform:uppercase;color:#3d4249}
  .photo-handshake{position:absolute;left:200px;top:365px;width:160px;height:92px;
    background:linear-gradient(120deg,#8fa9cf 0%,#4c6b9f 55%,#20355f 100%)}

  .core{position:absolute;left:24px;top:122px}
  .h-sub{font-size:11px;font-weight:700;text-transform:uppercase;color:#3d4249}
  .core .copy{margin-top:3px;width:330px}
  .tiles{position:absolute;left:24px;right:24px;top:162px;display:flex;gap:8px}
  .tile{flex:1;height:80px;position:relative}
  .tile span{position:absolute;left:0;right:0;bottom:0;background:var(--brand);color:#fff;font-size:6.5px;text-align:center;padding:3px 0}
  .tile--bm{background:linear-gradient(160deg,#cfe3f5,#5d8fc7)}
  .tile--fm{background:linear-gradient(160deg,#e6ecef,#9fb1bb)}
  .tile--ct{background:linear-gradient(160deg,#f1efe9,#b8b2a5)}
  .value{position:absolute;left:24px;top:262px;width:170px}
  .value .copy{margin-top:5px}
  .checklist{position:absolute;left:210px;top:262px;list-style:none;font-size:7px;line-height:2}
  .checklist li{display:flex;align-items:center;gap:5px}
  .checklist svg{width:8px;height:8px}
  .cta{position:absolute;left:210px;top:392px;width:146px;background:var(--brand);color:#fff;
    font-size:7px;font-weight:600;line-height:1.45;padding:9px 10px}
  .photo-collage{position:absolute;left:24px;top:360px;width:170px;height:110px;
    background:linear-gradient(135deg,#c9d3dc 0%,#8ea0b2 50%,#4f6a86 100%)}
</style>
</head>
<body>

<section class="spread spread--cover">
  <article class="page back">
    <div class="back__city" role="img" aria-label="Faded city skyline photograph"></div>
    <p class="back__motto">Quality<br>Service<br>Integrity</p>
    <p class="back__name">Harlow Property Solutions</p>
    <p class="back__contact">info@harlowpropertysolutions.com.au &nbsp;|&nbsp; www.harlowpropertysolutions.com.au<br>Harbourside and surrounding suburbs through to the Kestrel Peninsula</p>
  </article>
  <article class="page front">
    <p class="front__name">Harlow Property Solutions</p>
    <div class="front__photo" role="img" aria-label="City skyline at dusk reflected in a river"></div>
    <h1 class="front__tagline">Quality <small>Service</small><br><small>with</small> Integrity</h1>
    <p class="front__url">www.harlowpropertysolutions.com.au</p>
  </article>
</section>

<section class="spread spread--inside">
  <article class="page">
    <div class="band" role="img" aria-label="Night city skyline photograph"><h2 class="band__title">Vision</h2></div>
    <div class="vision copy">
      <p>At HPS, our aim is to provide complete solutions for Building and Facilities Owners and Strata Corporations in the management of their assets. With the understanding that each property has different needs and requirements, our focus is to work with clients to tailor solutions best suited to their specific needs.</p>
      <p>Our aim is to ensure the Building and Facilities are managed to the highest standards using the latest technological management solutions to efficiently and effectively control all aspects of the building. With a keen focus on controlling costs to ensure funds are spent cost-effectively, through improved operations and management of all aspects of the building.</p>
    </div>
    <h2 class="h-section">Key Aspects</h2>
    <div class="aspects aspects--a copy">
      <p class="aspect"><b>Compliance</b> with relevant industry acts and regulations</p>
      <p class="aspect"><b>OH&amp;S</b> to ensure the building and aspects are controlled safely and the risk of all contractors and owners is reduced and managed.</p>
      <p class="aspect"><b>Preventative Maintenance</b> to ensure assets are professionally maintained to ensure the best reliability and longevity of each asset.</p>
      <p class="aspect"><b>Reactive Maintenance</b> to ensure any issues that arise are resolved and handled as efficiently as possible.</p>
    </div>
    <div class="aspects aspects--b copy">
      <p class="aspect"><b>Communication</b> to ensure the Committee and Owners have clear and concise information and knowledge of the aspects of their building and assets</p>
      <p class="aspect"><b>Relationships</b> are a top priority as they are paramount for effective management with Owners, Residents, Developers and Strata Managers</p>
    </div>
    <div class="photo-handshake" role="img" aria-label="Business handshake photograph"></div>
  </article>

  <article class="page">
    <div class="band" role="img" aria-label="Night city skyline photograph"><h2 class="band__title">Services</h2></div>
    <div class="core">
      <h3 class="h-sub">Core Services</h3>
      <p class="copy">These are the core focus of the business to provide the highest standard in Building and Facilities Management.</p>
    </div>
    <div class="tiles">
      <div class="tile tile--bm" role="img" aria-label="Glass office tower photograph"><span>Building Management</span></div>
      <div class="tile tile--fm" role="img" aria-label="Modern lobby interior photograph"><span>Facilities Management</span></div>
      <div class="tile tile--ct" role="img" aria-label="Office interior photograph"><span>Caretaker</span></div>
    </div>
    <div class="value">
      <h3 class="h-sub">Value Added Services</h3>
      <p class="copy">In addition to the Core Service we are proud to offer these Value Added services to complement the management of the Building, or offer as stand-alone services to assist owners with the management of their Building and Assets.</p>
    </div>
    <ul class="checklist">
      <li><svg viewBox="0 0 8 8"><rect x=".5" y=".5" width="7" height="7" fill="none" stroke="#2a9fd8"/><path d="M2 4l1.5 1.5L6 2.5" fill="none" stroke="#2a9fd8"/></svg>Concierge</li>
      <li><svg viewBox="0 0 8 8"><rect x=".5" y=".5" width="7" height="7" fill="none" stroke="#2a9fd8"/><path d="M2 4l1.5 1.5L6 2.5" fill="none" stroke="#2a9fd8"/></svg>Cleaning</li>
      <li><svg viewBox="0 0 8 8"><rect x=".5" y=".5" width="7" height="7" fill="none" stroke="#2a9fd8"/><path d="M2 4l1.5 1.5L6 2.5" fill="none" stroke="#2a9fd8"/></svg>Project Management</li>
      <li><svg viewBox="0 0 8 8"><rect x=".5" y=".5" width="7" height="7" fill="none" stroke="#2a9fd8"/><path d="M2 4l1.5 1.5L6 2.5" fill="none" stroke="#2a9fd8"/></svg>Electrical</li>
      <li><svg viewBox="0 0 8 8"><rect x=".5" y=".5" width="7" height="7" fill="none" stroke="#2a9fd8"/><path d="M2 4l1.5 1.5L6 2.5" fill="none" stroke="#2a9fd8"/></svg>Handyman</li>
      <li><svg viewBox="0 0 8 8"><rect x=".5" y=".5" width="7" height="7" fill="none" stroke="#2a9fd8"/><path d="M2 4l1.5 1.5L6 2.5" fill="none" stroke="#2a9fd8"/></svg>New site setup</li>
      <li><svg viewBox="0 0 8 8"><rect x=".5" y=".5" width="7" height="7" fill="none" stroke="#2a9fd8"/><path d="M2 4l1.5 1.5L6 2.5" fill="none" stroke="#2a9fd8"/></svg>Building defect management</li>
    </ul>
    <p class="cta">Please feel free to contact us to enquire about any of the above services, either individually or as multiple services to ensure the best value can be provided for your requirements.</p>
    <div class="photo-collage" role="img" aria-label="Collage of service photographs: cleaning, electrical, meetings and plans"></div>
  </article>
</section>

</body>
</html>
```